Disability and mental health support work company requires business card

Specialising
Wrenfield Disability is a new QCAP service aimed toward QCAP participants with a history of criminal justice, psychosocial/mental health, intellectual, and cognitive disabilities.

Our focus
Focusing on providing core QCAP supports for community participation, daily activities and supported independent living.

Authentic
Likeminded people wanting to make a difference in participant's lives.

Our aim to provide holistic and empowering supports targeted towards creating independence and guidance for all participants and families.
Over 35 years of experience working with people that have psychosocial, intellectual, and cognitive disabilities.

Industry/Entity Type

disability and mental health

Contact Information for Business Card

logo - business name

Colors
0054AA
0677BA
7BADD7
CADEEF
E8F1F8
FFF300
FFF600
FEFA6F
FFFEC7
FFFEE8

Requirements
Must have
• want double sided business cards(wont let me change it)
Should not have
• any disability related pictures

```html
<!DOCTYPE html>
<html lang="en">
<head>
<meta charset="utf-8">
<title>Wrenfield Disability – Business Card</title>
<link rel="stylesheet" href="https://fonts.googleapis.com/css2?family=Poppins:ital,wght@0,400;0,600;1,400&display=swap">
<style>
  :root {
    --page-bg: #e9e6e2;
    --card-top: #f4f6f8;
    --card-bottom: #e3e8ed;
    --navy: #1b3a66;
    --sky: #7badd7;
    --gold: #e1b12a;
    --ink: #1f3658;
    --name-tint: #a9c7e6;
    --title-tint: #e4edf6;
    --icon: #8aa4bf;
  }
  html, body {
    margin: 0;
    width: 1200px;
    height: 1054px;
    overflow: hidden;
    background: var(--page-bg);
    font-family: "Poppins", sans-serif;
  }
  .card {
    position: absolute;
    left: 100px;
    top: 226px;
    width: 1000px;
    height: 603px;
    border-radius: 26px;
    overflow: hidden;
    background: linear-gradient(160deg, var(--card-top), var(--card-bottom));
    box-shadow: 0 10px 30px rgba(0,0,0,0.12);
  }
  .header-band {
    position: absolute;
    left: 0;
    top: 0;
    width: 100%;
    height: 160px;
    background: var(--navy);
  }
  .header-rule {
    position: absolute;
    left: 0;
    top: 172px;
    width: 100%;
    height: 8px;
    background: var(--gold);
  }
  .holder {
    position: absolute;
    right: 50px;
    top: 54px;
    text-align: right;
  }
  .holder-name {
    margin: 0;
    font-weight: 600;
    font-size: 36px;
    letter-spacing: 1px;
    color: var(--name-tint);
    line-height: 1.2;
  }
  .holder-title {
    margin: 0;
    font-style: italic;
    font-size: 24px;
    color: var(--title-tint);
    line-height: 1.3;
  }
  .brand {
    position: absolute;
    left: 94px;
    top: 215px;
    width: 330px;
    height: 330px;
    border-radius: 50%;
    background: var(--navy);
    display: flex;
    align-items: center;
    justify-content: center;
    text-align: center;
  }
  .brand-name {
    font-weight: 600;
    font-size: 34px;
    line-height: 1.2;
    color: var(--name-tint);
    margin: 0;
  }
  .contact {
    position: absolute;
    right: 48px;
    top: 328px;
    text-align: right;
    color: var(--ink);
    font-size: 23px;
    line-height: 1.7;
    font-style: normal;
  }
  .address { margin: 0 0 14px; }
  .contact-line {
    display: flex;
    justify-content: flex-end;
    align-items: center;
    gap: 18px;
    margin: 0;
  }
  .contact-line svg {
    width: 24px;
    height: 24px;
    fill: var(--icon);
    flex: none;
  }
</style>
</head>
<body>
  <article class="card">
    <div class="header-band"></div>
    <div class="header-rule"></div>

    <header class="holder">
      <h1 class="holder-name">DANIEL HARTLEY</h1>
      <p class="holder-title">Managing Director</p>
    </header>

    <div class="brand">
      <p class="brand-name">Wrenfield<br>Disability</p>
    </div>

    <address class="contact">
      <p class="address">87 Linden Row, Maple City,<br>Fairview, US 204518</p>
      <p class="contact-line">020-0303-0404
        <svg viewBox="0 0 24 24"><path d="M3 9c0-3 4-5 9-5s9 2 9 5l-4 1-1-3H8L7 10 3 9zm4 2h10l3 8H4l3-8zm5 2a2.5 2.5 0 1 0 0 5 2.5 2.5 0 0 0 0-5z"/></svg>
      </p>
      <p class="contact-line">daniel@wrenfielddisability.com
        <svg viewBox="0 0 24 24"><path d="M2 5h20v14H2zM3.5 6.5 12 13l8.5-6.5z"/></svg>
      </p>
      <p class="contact-line">www.wrenfielddisability.com
        <svg viewBox="0 0 24 24"><path d="M12 2a10 10 0 1 0 0 20 10 10 0 0 0 0-20zm0 2c1.3 1.5 2.2 3.6 2.4 7H9.6C9.8 7.6 10.7 5.5 12 4zM4.1 11a8 8 0 0 1 4.2-6.1c-.9 1.7-1.5 3.8-1.6 6.1zm0 2h2.6c.1 2.300.7 4.4 1.6 6.1A8 8 0 0 1 4.1 13zm5.5 0h4.8c-.2 3.4-1.1 5.5-2.4 7-1.3-1.5-2.2-3.6-2.4-7zm6.1 6.1c.9-1.7 1.5-3.8 1.6-6.1h2.6a8 8 0 0 1-4.2 6.1zM17.3 11c-.1-2.3-.7-4.4-1.6-6.1a8 8 0 0 1 4.2 6.1z"/></svg>
      </p>
    </address>
  </article>
</body>
</html>
```